In need a simple business/calling card

I am looking for a VERY simple, professional, and classic business card which is really more of a calling card. In the Hartwell & Pryce or Lorvik kind of style. I am also open to a solid boarder but not necessary. I prefer no logos or "designs".

Target Market(s)

general

Contact Information for Business Card

Daniel Whitcombe (or Daniel R. Whitcombe)
+1 555 274 8163
dan@whitcombe.example

Thats it!

Font styles to use
Serif
Sans Serif
Script

Colors

Designer to choose colors to be used in the design.

Requirements
Must have
• everything on the card details section.
Nice to have
• n/a
Should not have
• No logos.

```html
<!DOCTYPE html>
<html lang="en">
<head>
<meta charset="utf-8">
<title>Daniel Whitcombe – Calling Card</title>
<link rel="stylesheet" href="https://fonts.googleapis.com/css2?family=Marcellus+SC&family=Roboto:wght@400&display=swap">
<style>
  :root {
    --backdrop: #e6e7ea;
    --card-navy: #2a4377;
    --card-navy-light: #2d4a86;
    --ink: #ffffff;
    --rule: rgba(255, 255, 255, 0.85);
  }
  html, body {
    margin: 0;
    padding: 0;
    width: 1200px;
    height: 1200px;
    overflow: hidden;
    background: var(--backdrop);
  }
  .calling-card {
    position: absolute;
    left: 180px;
    top: 362px;
    width: 840px;
    height: 477px;
    background: radial-gradient(ellipse at 52% 45%, var(--card-navy-light) 0%, var(--card-navy) 70%);
    color: var(--ink);
  }
  .divider {
    position: absolute;
    left: 292px;
    width: 316px;
    height: 16px;
  }
  .divider--top { top: 135px; }
  .divider--bottom { top: 279px; }
  .divider__rule {
    position: absolute;
    top: 7px;
    height: 1.5px;
  }
  .divider__rule--left {
    left: 0;
    width: 122px;
    background: linear-gradient(to right, rgba(255,255,255,0), var(--rule));
  }
  .divider__rule--right {
    right: 0;
    width: 136px;
    background: linear-gradient(to left, rgba(255,255,255,0), var(--rule));
  }
  .divider__flourish {
    position: absolute;
    left: 126px;
    top: 3px;
    width: 52px;
    height: 10px;
    border-radius: 5px;
    background: rgba(255, 255, 255, 0.55);
  }
  .card-name {
    position: absolute;
    left: 0;
    right: 0;
    top: 178px;
    margin: 0;
    padding-left: 46px;
    text-align: center;
    font-family: "Marcellus SC", serif;
    font-weight: 400;
    font-size: 54px;
    line-height: 1;
    letter-spacing: 0.5px;
  }
  .card-contact {
    position: absolute;
    top: 387px;
    margin: 0;
    font-family: "Roboto", sans-serif;
    font-size: 28px;
    line-height: 1;
  }
  .card-contact--phone { left: 88px; }
  .card-contact--email { right: 78px; }
</style>
</head>
<body>
  <main class="calling-card">
    <div class="divider divider--top">
      <span class="divider__rule divider__rule--left"></span>
      <span class="divider__flourish" role="img" aria-label="Small decorative scroll flourish"></span>
      <span class="divider__rule divider__rule--right"></span>
    </div>

    <h1 class="card-name">Daniel Whitcombe</h1>

    <div class="divider divider--bottom">
      <span class="divider__rule divider__rule--left"></span>
      <span class="divider__flourish" role="img" aria-label="Small decorative scroll flourish"></span>
      <span class="divider__rule divider__rule--right"></span>
    </div>

    <p class="card-contact card-contact--phone">555.274.8163</p>
    <p class="card-contact card-contact--email">dan@whitcombe.example</p>
  </main>
</body>
</html>
```